Website Design for Door Distributor

Granite Hinge Works LLC distributes doors in the Southwestern region of the United States. We need a website design for our company launch.

We are looking for a website design that screams modern, and is easy to navigate. We want our customers to browse through our collections of doors with ease, while at the same time enjoy the feel of the website (more on how the website should feel below). Our logo is attached to help with the design process.

We expect this relationship to continue beyond the initial assignment, whether it includes additions or updates to the site. In that sense, we will only work with that designer who will specifically incorporate our ideas into the design, not a designer that submits a "one-size-fits-all" design. With that in mind, we are looking for a creative person who is willing to take some risks.

We are committed to minimizing the amount of revisions needed, so we encourage you to message us with any questions you may have throughout the process, especially in the earlier phases.

Thanks in advance for your time.

Target Market(s)

Home builders, commercial builders, developers, and upper-middle class/upper class customers. As you can see, our target market is of a more sophisticated type, so the design should be on the more serious side, and less playful. It should showcase a sense of class.

Industry/Entity Type

Requirements
Must have
• The home page should have a slideshow showcasing 4 to 5 different topics. See www.quillbranch.net for an example. The headings for each picture should be easily customizable (font, color, etc.). The user should also be able to click on the picture and be taken to the page that the pictures are linked to.

At the very top right of every page, there should be 2 header links: Download Brochure | Contact

There should be 5 static categories placed in one row at the top of each page. See www.morvik-tane.com for an example. Each of these categories should drop down when you rest your mouse over it and display a list of links. Again, this should be easily customizable and shown on every page of the site. This will serve as the navigation menu. Let us know if you need to know the exact amount of links for each category - hopefully we can customize it on our end fairly easily.

Categories: Home | Products | Gallery | Support | About Us

Home Page: Along with the above, the home page should include a welcome section that introduces the user to the site. There should also be sections for "Featured Product" and "Testimonial".

Featured product: this will include an image and short text.

Testimonial: this will include a quote, which should be easy for us to update weekly, and a link to "More Testimonials".
Should not have
• No clutter - instead, the design layout should be open and easy to navigate.

No cartoonish graphics - instead, the graphics should be sophisticated and modern.

No flash, no java.

```html
<!DOCTYPE html>
<html lang="en">
<head>
<meta charset="utf-8">
<title>Granite Hinge Works — Home</title>
<link href="https://fonts.googleapis.com/css2?family=Oswald:wght@200;300&family=Crimson+Text:ital@0;1&family=Arimo:wght@400;700&family=Roboto+Condensed:wght@400&display=swap" rel="stylesheet">
<style>
:root{
  --brown:#7b4a26;
  --brown-dark:#5c3216;
  --brown-light:#a0683c;
  --title:#8a5632;
  --footer:#3b1f0e;
  --ink:#333;
  --rule:#e1e1e1;
  --band:#ececec;
  --band-alt:#efefef;
  --white:#fff;
}
*{box-sizing:border-box;margin:0;padding:0}
html,body{width:936px;height:1200px;overflow:hidden}
body{font-family:"Arimo",Arial,sans-serif;color:var(--ink);background:var(--white)}
.page{position:relative;width:936px;height:1200px;overflow:hidden}
.abs{position:absolute}

/* header */
.site-header{left:0;top:0;width:936px;height:103px;background:var(--white);border-top:2px solid var(--brown);border-bottom:1px solid var(--rule)}
.utility-bar{left:625px;top:0;width:218px;height:29px;background:linear-gradient(var(--brown-light),var(--brown));display:flex;align-items:center;justify-content:space-around;font-size:8.5px;color:var(--white);letter-spacing:.2px;padding:0 8px}
.utility-bar span{display:flex;align-items:center;gap:6px}
.brand{left:93px;top:18px;display:flex;align-items:center;gap:10px}
.brand-mark{width:14px;height:14px;background:var(--brown)}
.brand-name{font-family:"Crimson Text",serif;font-size:18px;color:var(--brown);letter-spacing:.5px}
.main-nav{top:61px;height:38px;display:flex}
.main-nav a{display:flex;align-items:center;justify-content:center;height:38px;font-size:10px;color:#444;text-decoration:none;letter-spacing:.3px;border-left:1px solid var(--rule)}
.main-nav a.first{border-left:none}
.main-nav a.active{color:var(--brown-light);border:1px solid #d8d8d8;border-bottom:none;background:var(--white)}
.dropdown{left:520px;top:99px;width:165px;height:144px;background:var(--white);box-shadow:0 1px 4px rgba(0,0,0,.2);padding:6px 12px;z-index:5}
.dropdown li{list-style:none;font-size:8.5px;color:#444;height:25.6px;line-height:25.6px;border-bottom:1px solid var(--rule)}

/* hero */
.hero-band{left:0;top:103px;width:936px;height:386px;background:var(--band)}
.hero-card{left:93px;top:124px;width:750px;height:345px;background:var(--white);box-shadow:0 1px 3px rgba(0,0,0,.15)}
.hero-divider{left:372px;top:142px;width:1px;height:310px;background:var(--rule)}
.hero-copy{left:97px;top:208px;width:280px;text-align:center;z-index:2}
.hero-title{font-family:"Oswald",sans-serif;font-weight:300;font-size:24px;line-height:30px;color:#444;white-space:nowrap}
.hero-text{font-family:"Roboto Condensed",sans-serif;font-size:9.5px;line-height:17px;color:#333;margin-top:12px;white-space:nowrap}
.btn{display:inline-flex;margin-top:20px;width:108px;height:33px;background:linear-gradient(var(--brown-light),var(--brown-dark));color:var(--white);font-size:9px;align-items:center;justify-content:center;gap:8px;border-radius:2px}
.hero-photo{left:387px;top:132px;width:446px;height:328px;background:linear-gradient(135deg,#6a3f1e 0%,#b07a48 45%,#d9b07c 60%,#4a2a12 100%)}
.slide-arrow{top:275px;width:31px;height:36px;background:rgba(255,255,255,.9);display:flex;align-items:center;justify-content:center;border:1px solid #ddd}

/* section heads */
.section-head{left:92px;width:751px;display:flex;align-items:center;gap:16px}
.section-title{font-family:"Oswald",sans-serif;font-weight:200;font-size:25px;line-height:32px;color:var(--title);white-space:nowrap}
.section-rule{flex:1;height:4px;background:var(--rule)}
.section-link{font-size:9.5px;color:var(--brown);white-space:nowrap}

/* featured */
.product-card{top:552px;width:171px;height:196px;border:1px solid #ddd;padding:5px;background:var(--white)}
.product-photo{width:100%;height:100%;background:linear-gradient(90deg,#e9e9e9 0%,#e9e9e9 28%,#9a6a3c 32%,#9a6a3c 68%,#e9e9e9 72%,#e9e9e9 100%)}
.product-label{top:758px;font-size:9.5px;color:#444;letter-spacing:.3px}

/* testimonials */
.testimonial-band{left:0;top:788px;width:936px;height:352px;background:var(--band-alt)}
.avatar{width:78px;height:78px;border-radius:50%;background:radial-gradient(circle at 50% 40%,#9a8a80,#3a3a3a);border:2px solid var(--white);box-shadow:0 0 0 1px #ccc}
.person-name{font-family:"Crimson Text",serif;font-style:italic;font-size:17px;color:var(--brown)}
.person-role{font-size:8.5px;color:#444;margin-top:2px}
.social{display:flex;gap:7px;margin-top:8px}
.social i{width:22px;height:22px;border-radius:50%;border:1px solid #d8c0a8;background:var(--white);display:flex;align-items:center;justify-content:center}
.social i b{display:block;width:9px;height:9px;border-radius:50%;background:var(--brown-light)}
.testimonial-text{width:330px;font-size:8.8px;line-height:15.3px;color:#333}
.col-divider{left:465px;top:848px;width:1px;height:185px;background:#ddd}
.quote-rule{left:173px;top:1051px;width:587px;height:1px;background:#ddd}
.pull-quote{left:0;top:1072px;width:936px;text-align:center}
.pull-quote p{font-size:13px;color:#222}
.pull-quote cite{display:block;font-size:8.5px;font-style:italic;color:#444;margin-top:9px}
.quote-mark{top:1064px;font-family:Georgia,serif;font-size:46px;line-height:1;color:#d6d6d6}

/* footer */
.site-footer{left:0;top:1140px;width:936px;height:60px;background:var(--footer)}
.site-footer p{position:absolute;right:93px;top:25px;font-size:8.5px;color:#eee}
</style>
</head>
<body>
<div class="page">

  <header class="site-header abs"></header>
  <div class="utility-bar abs">
    <span>
      <svg width="8" height="9" viewBox="0 0 8 9"><path d="M4 0v6M1 3.5 4 6.5 7 3.5M0 8.5h8" stroke="#fff" stroke-width="1.2" fill="none"/></svg>
      DOWNLOAD BROCHURE
    </span>
    <span>
      <svg width="12" height="9" viewBox="0 0 12 9"><rect x=".5" y=".5" width="11" height="8" fill="none" stroke="#fff"/><path d="M.5 .5 6 5l5.5-4.5" stroke="#fff" fill="none"/></svg>
      CONTACT
    </span>
  </div>

  <div class="brand abs">
    <span class="brand-mark"></span>
    <span class="brand-name">Granite Hinge Works</span>
  </div>

  <nav class="main-nav abs" style="left:455px">
    <a class="first" style="width:65px">HOME</a>
    <a class="active" style="width:92px">PRODUCTS</a>
    <a style="width:80px;border-left:none">GALLERY</a>
    <a style="width:84px">SUPPORT</a>
    <a style="width:80px">ABOUT US</a>
  </nav>
  <ul class="dropdown abs">
    <li>LOREM IPSUM DOLOR</li>
    <li>LOREM IPSUM DOLOR</li>
    <li>LOREM IPSUM DOLOR</li>
    <li>LOREM IPSUM DOLOR</li>
    <li>LOREM IPSUM DOLOR</li>
  </ul>

  <section class="hero-band abs"></section>
  <div class="hero-card abs"></div>
  <div class="hero-divider abs"></div>
  <div class="hero-photo abs" role="img" aria-label="Modern glass and bronze entrance doors of a commercial building lobby"></div>
  <div class="slide-arrow abs" style="left:93px">
    <svg width="10" height="22" viewBox="0 0 10 22"><path d="M9 1 1 11l8 10" stroke="#888" fill="none"/></svg>
  </div>
  <div class="slide-arrow abs" style="left:812px">
    <svg width="10" height="22" viewBox="0 0 10 22"><path d="M1 1l8 10-8 10" stroke="#888" fill="none"/></svg>
  </div>
  <div class="hero-copy abs">
    <h1 class="hero-title">U.S.A MADE MODERN DOOR</h1>
    <p class="hero-text">Lorem ipsum is simply a dummy text of the printing and<br>typesetting industry.</p>
    <div class="btn">Learn More
      <svg width="5" height="8" viewBox="0 0 5 8"><path d="M1 1l3 3-3 3" stroke="#fff" fill="none"/></svg>
    </div>
  </div>

  <div class="section-head abs" style="top:504px">
    <h2 class="section-title">FEATURED</h2>
    <div class="section-rule"></div>
    <span class="section-link">See all products &nbsp;›</span>
  </div>

  <div class="product-card abs" style="left:93px"><div class="product-photo" role="img" aria-label="Dark mahogany nine-panel door"></div></div>
  <div class="product-card abs" style="left:285px"><div class="product-photo" role="img" aria-label="Light oak shaker panel door"></div></div>
  <div class="product-card abs" style="left:477px"><div class="product-photo" role="img" aria-label="Walnut door with six glass lites"></div></div>
  <div class="product-card abs" style="left:669px"><div class="product-photo" role="img" aria-label="Pine door with two upper glass panes"></div></div>
  <span class="product-label abs" style="left:93px">LOREM IPSUM DOLOR</span>
  <span class="product-label abs" style="left:285px">LOREM IPSUM DOLOR</span>
  <span class="product-label abs" style="left:477px">LOREM IPSUM DOLOR</span>
  <span class="product-label abs" style="left:670px">LOREM IPSUM DOLOR</span>

  <section class="testimonial-band abs"></section>
  <div class="section-head abs" style="top:804px">
    <h2 class="section-title">TESTIMONIALS</h2>
    <div class="section-rule"></div>
    <span class="section-link">All Testimonials &nbsp;›</span>
  </div>

  <div class="avatar abs" style="left:92px;top:856px" role="img" aria-label="Portrait of Reid Calloway"></div>
  <div class="abs" style="left:196px;top:865px">
    <div class="person-name">Reid Calloway</div>
    <div class="person-role">( C.E.O Company name)</div>
    <div class="social"><i><b></b></i><i><svg width="11" height="8" viewBox="0 0 11 8"><rect x=".5" y=".5" width="10" height="7" fill="none" stroke="#a0683c"/><path d="M.5 .5 5.5 4.5 10.5.5" stroke="#a0683c" fill="none"/></svg></i></div>
  </div>
  <p class="testimonial-text abs" style="left:91px;top:947px">Lorem ipsum is simply a dummy text of the printing and typesetting industry. Lorem ipsum has been the industry's standard dummy text ever since the 1500s, when an unknown printer took a gallery of type and scrambled it to make a type specimen look</p>

  <div class="col-divider abs"></div>

  <div class="avatar abs" style="left:516px;top:856px" role="img" aria-label="Portrait of Maren Ashby"></div>
  <div class="abs" style="left:620px;top:865px">
    <div class="person-name">Maren Ashby</div>
    <div class="person-role">( C.E.O Company name)</div>
    <div class="social"><i><b></b></i><i><svg width="11" height="8" viewBox="0 0 11 8"><rect x=".5" y=".5" width="10" height="7" fill="none" stroke="#a0683c"/><path d="M.5 .5 5.5 4.5 10.5.5" stroke="#a0683c" fill="none"/></svg></i></div>
  </div>
  <p class="testimonial-text abs" style="left:515px;top:947px">Lorem ipsum is simply a dummy text of the printing and typesetting industry. Lorem ipsum has been the industry's standard dummy text ever since the 1500s, when an unknown printer took a gallery of type and scrambled it to make a type specimen look</p>

  <div class="quote-rule abs"></div>
  <span class="quote-mark abs" style="left:212px">“</span>
  <span class="quote-mark abs" style="left:698px">”</span>
  <blockquote class="pull-quote abs">
    <p>Lorem ipsum is simply a dummy text of the printing and typesetting industry.</p>
    <cite>By Elliot Varga</cite>
  </blockquote>

  <footer class="site-footer abs">
    <p>© 2014 Granite Hinge Works, all rights reserved</p>
  </footer>

</div>
</body>
</html>
```